Simple but elegant business card/logo design for exclusive beauty business

We need a logo designed for a new elegant and exclusive beauty business called "R". The logo itself should be a stylistic and custom design for the letter "R". We would like the business card to have the logo as the centrepiece on a clean background. Gold Logo on black background or silver on white background.

The business card details should be displayed centre of the card. Details are as follows:

Tamsin Earle
Facebook: /shinesoftlyr
Instagram: /shinesoftlyr

The words "Shine Softly" should also appear somewhere on the card.

Industry/Entity Type

Business

Logo Text

G

Requirements
Must have
• Design must be simple, clean and elegant
Should not have
• The design should not be cluttered

```html
<!DOCTYPE html>
<html lang="en">
<head>
<meta charset="utf-8">
<title>Tamsin Earle – Business Card</title>
<link rel="stylesheet" href="https://fonts.googleapis.com/css2?family=Raleway:wght@300;400&family=Pinyon+Script&display=swap">
<style>
  :root {
    --gold: #d4b855;
    --black: #000000;
    --silver-light: #ffffff;
    --silver-mid: #e4e5e7;
    --silver-dark: #cfd0d3;
    --stone: #b9babb;
  }
  * { margin: 0; padding: 0; box-sizing: border-box; }
  html, body { width: 1200px; height: 1200px; overflow: hidden; }
  body { position: relative; background: var(--black); font-family: 'Raleway', sans-serif; }

  .presentation-top {
    position: absolute; left: 0; top: 0; width: 1200px; height: 507px;
    background: radial-gradient(ellipse 60% 55% at 50% 50%, var(--silver-light) 0%, var(--silver-mid) 70%, var(--silver-dark) 100%);
  }
  .card {
    position: absolute; top: 72px; width: 573px; height: 344px;
    background: var(--black);
  }
  .card--front { left: 20px; }
  .card--back { left: 610px; }

  .monogram {
    position: absolute; left: 0; right: 0; top: 50%;
    transform: translateY(-50%);
    text-align: center; color: var(--gold);
    font-family: 'Raleway', sans-serif; font-weight: 300;
    line-height: 1;
  }
  .card--front .monogram { font-size: 170px; }

  .rule {
    position: absolute; height: 2px; background: var(--gold);
  }
  .rule--top { left: 29px; right: 26px; top: 27px; }
  .rule--bottom-left { left: 29px; width: 185px; top: 314px; }
  .rule--bottom-right { right: 26px; width: 185px; top: 314px; }
  .dot {
    position: absolute; top: 311px; width: 8px; height: 8px;
    border-radius: 50%; background: var(--gold);
  }
  .dot--left { left: 219px; }
  .dot--right { right: 216px; }
  .tagline {
    position: absolute; left: 0; right: 0; top: 296px;
    text-align: center; color: var(--gold);
    font-family: 'Pinyon Script', cursive; font-size: 21px;
  }

  .contact {
    position: absolute; left: 0; right: 0; top: 112px;
    text-align: center; color: var(--gold);
  }
  .contact__name {
    font-weight: 400; font-size: 43px; letter-spacing: 2px; line-height: 1;
  }
  .contact__handles { list-style: none; margin-top: 14px; }
  .contact__handle {
    display: flex; justify-content: center; align-items: center; gap: 8px;
    font-weight: 300; font-size: 22px; line-height: 33px;
  }
  .contact__marker {
    width: 22px; height: 22px; border: 1.5px solid var(--gold); border-radius: 50%;
  }

  .presentation-bottom-plain {
    position: absolute; left: 0; top: 540px; width: 693px; height: 660px;
    background: var(--stone);
  }
  .logo-panel {
    position: absolute; left: 693px; top: 540px; width: 507px; height: 660px;
    background: var(--black);
  }
  .logo-panel .monogram { font-size: 360px; }
</style>
</head>
<body>
  <section class="presentation-top">
    <div class="card card--front">
      <div class="monogram">R</div>
    </div>
    <div class="card card--back">
      <div class="rule rule--top"></div>
      <div class="contact">
        <h1 class="contact__name">TAMSIN EARLE</h1>
        <ul class="contact__handles">
          <li class="contact__handle"><span class="contact__marker"></span>shinesoftlyr</li>
          <li class="contact__handle"><span class="contact__marker"></span>shinesoftlyr</li>
        </ul>
      </div>
      <div class="rule rule--bottom-left"></div>
      <span class="dot dot--left"></span>
      <p class="tagline">Shine Softly</p>
      <span class="dot dot--right"></span>
      <div class="rule rule--bottom-right"></div>
    </div>
  </section>

  <div class="presentation-bottom-plain"></div>
  <section class="logo-panel">
    <div class="monogram">R</div>
  </section>
</body>
</html>
```